Website Banner Ad Design - 4x 200x200px panels that will rotate

I'm looking for four (4) 200x200px "panels" that will rotate on a website. Each one should have a unique description or key words on it, that makes it attractive to customers. It is important that each individual one kinda fits to our logo design to give it a "uniform" design.
The first panel should just be our logo and a slogan that says "AFFORDABLE. ACCELERATED. EFFECTIVE." This panel should also list our website "www.torvenix.com"
The second panel should have the following key text:
- Accelerated Training Courses
- Private Pilot in 4-weeks
- Career Programs from PPL to CFII
- Pay-as-you-go
The third panel should have the following key text:
- Advanced Training
- Firefighting (QPRA) & Forestry Tactics Training
- KX 310 & Tarn 118K Turbine Transition Training
- External-Load (VR) Courses
THE fourth panel should list our website address "www.torvenix.com" and phone number: (555) 482-7093.
I give free hand with the design. Any idea is welcome. See attached some photos and logo that can be used. If you visit http://www.quillmarshpost.com/FLIGHTTRAINING/tabid/421/Default.aspx you can see other 200x200 panels to get an idea of what we're looking for. Our look has to be professional and stick out from the rest of our competitors. By questions, just PM me.

```html
<!DOCTYPE html>
<html lang="en">
<head>
<meta charset="utf-8">
<title>Accelerated Training Panel</title>
<link rel="stylesheet" href="https://fonts.googleapis.com/css2?family=Encode+Sans+Condensed:wght@300&display=swap">
<style>
  :root {
    --page: #ffffff;
    --disc: #d7d7d8;
    --scene: #e3e3e4;
    --ink: #2f6fb3;
    --marker: #86acd9;
  }
  html, body {
    margin: 0;
    padding: 0;
    width: 1200px;
    height: 1200px;
    overflow: hidden;
    background: var(--page);
  }
  .panel {
    display: block;
    width: 1200px;
    height: 1200px;
  }
  .panel-disc { fill: var(--disc); }
  .panel-scene { fill: var(--scene); opacity: 0.55; }
  .bullet-marker { fill: var(--marker); }
  .bullet-text {
    fill: var(--ink);
    font-family: "Encode Sans Condensed", "Arial Narrow", sans-serif;
    font-weight: 300;
    font-size: 152px;
  }
</style>
</head>
<body>
<svg class="panel" viewBox="0 0 1200 1200" xmlns="http://www.w3.org/2000/svg" role="group" aria-label="Accelerated training courses panel">
  <circle class="panel-disc" cx="600" cy="600" r="598"/>
  <rect class="panel-scene" x="190" y="300" width="840" height="860" rx="40" role="img" aria-label="Faint pictogram of a helicopter on a whiteboard with an instructor beside it"/>

  <g class="bullet-list">
    <polygon class="bullet-marker" points="30,135 30,225 108,180"/>
    <text class="bullet-text" x="120" y="228" textLength="678" lengthAdjust="spacingAndGlyphs">Accelerated</text>
    <text class="bullet-text" x="124" y="354" textLength="942" lengthAdjust="spacingAndGlyphs">Training Courses</text>

    <polygon class="bullet-marker" points="30,409 30,499 108,454"/>
    <text class="bullet-text" x="124" y="502" textLength="816" lengthAdjust="spacingAndGlyphs">Private Pilot in</text>
    <text class="bullet-text" x="124" y="626" textLength="462" lengthAdjust="spacingAndGlyphs">4-weeks</text>

    <polygon class="bullet-marker" points="30,681 30,771 108,726"/>
    <text class="bullet-text" x="124" y="774" textLength="940" lengthAdjust="spacingAndGlyphs">Career Programs</text>
    <text class="bullet-text" x="124" y="898" textLength="908" lengthAdjust="spacingAndGlyphs">from PPL to CFII</text>

    <polygon class="bullet-marker" points="30,941 30,1031 108,986"/>
    <text class="bullet-text" x="124" y="1034" textLength="822" lengthAdjust="spacingAndGlyphs">Pay-as-you-go</text>
  </g>
</svg>
</body>
</html>
```